Home Services- Spring Clean Options

Brightwell Crew provides a variety of Home Services- focused on cleaning & improving the exterior of the home:

 Power Washing- driveways, sidewalks, patios, decks, fence
 Fence Staining- make fence look new with variety of staining colors
 Gutter cleaning- important to make sure have proper Water Drainage
 Gutter Guard Installation- prevent damage to roof and house by keeping debris out of gutters and water flowing.
 Window Washing- our exterior washing team and reach the highest windows
 Landscape& Patio Lights- highlight areas for beauty and safety
Updates

We are are almost finished. Just please make sure you pay attention to the wording and grammer in Red thx

Target Market(s)

Middle to Upper level Home Owners (especially women)

Industry/Entity Type

Cleaning Services

Font styles to use
Serif
Sans Serif

Requirements
Must have
• Not be Cluttered- Clean friendly, professional look. Focus on the Professional

Info@GoBrightwellCrew.com
972-648-0000
Nice to have
• Pictures of services- these are just examples
Should not have
• Bigger and bolder Services & Specials. Want to Show all the Services we offer but do Not use too much detail- don't want it to look "cluttered"

```html
<!DOCTYPE html>
<html lang="en">
<head>
<meta charset="utf-8">
<title>Brightwell Crew – Home Services Flyer</title>
<link rel="stylesheet" href="https://fonts.googleapis.com/css2?family=Lato:ital,wght@0,400;0,700;1,400&family=Tinos:wght@700&display=swap">
<style>
:root{
  --teal:#0e9577;
  --green:#8cbf1f;
  --green-light:#a6cc2a;
  --ink:#2a2a2a;
  --grey:#444;
  --page:#000;
  --white:#fff;
}
*{box-sizing:border-box;margin:0;padding:0}
html,body{width:1200px;height:1200px;overflow:hidden;background:var(--page)}
.flyer{position:absolute;left:233px;top:78px;width:794px;height:1028px;background:var(--white);overflow:hidden;font-family:"Lato",sans-serif}
.hero-photo{position:absolute;left:0;top:90px;width:794px;height:445px;background:linear-gradient(160deg,#5f7a45 0%,#8a9a78 35%,#b8b0a0 60%,#6f8b52 100%)}
.hero-mask{position:absolute;left:0;top:0;width:794px;height:560px}
.top-strip{position:absolute;left:0;top:0;width:100%;height:20px;background:var(--teal)}
.title-banner{position:absolute;left:0;top:0;width:794px;height:64px}
.brand-name{position:absolute;left:0;top:9px;width:794px;text-align:center;font-family:"Tinos",serif;font-weight:700;font-size:39px;line-height:44px;color:var(--white);letter-spacing:1px}
.tagline{position:absolute;left:0;top:71px;width:794px;text-align:center}
.tagline h2{font-weight:700;font-size:27px;color:var(--teal);line-height:30px}
.tagline p{font-style:italic;font-size:19px;color:var(--grey);line-height:24px}
.service-photo{position:absolute;width:120px;height:120px;border-radius:50%;border:4px solid var(--teal);box-shadow:0 0 0 4px var(--white),0 0 0 7px var(--green-light)}
.service-photo.green{border-color:var(--green)}
.service-label{position:absolute;height:32px;line-height:32px;font-family:"Tinos",serif;font-weight:700;font-size:16px;color:var(--white);letter-spacing:.5px;white-space:nowrap}
.service-label.left{padding-left:42px;clip-path:polygon(0 0,93% 0,100% 100%,0 100%)}
.service-label.right{padding-left:24px;clip-path:polygon(0 0,100% 0,100% 100%,4% 100%)}
.service-label.small{font-size:13.5px;letter-spacing:.3px}
.service-label.green{background:var(--green)}
.service-label.teal{background:var(--teal)}
.service-text{position:absolute;font-size:15px;line-height:18px;color:var(--ink)}
.service-text.right{text-align:right}
.footer{position:absolute;left:0;top:970px;width:794px;height:58px;background:linear-gradient(90deg,var(--teal) 0%,var(--green) 45%,var(--teal) 62%,var(--teal) 100%)}
.phone-pill{position:absolute;left:140px;top:14px;width:243px;height:30px;line-height:30px;border-radius:15px;background:var(--white);padding-left:34px;font-weight:700;font-size:22px;color:#111}
.call-label{position:absolute;left:0;top:14px;width:150px;height:30px;line-height:30px;padding-left:28px;border-radius:0 15px 15px 0;background:var(--teal);font-family:"Tinos",serif;font-weight:700;font-size:21px;color:var(--white)}
.website{position:absolute;right:46px;top:13px;font-family:"Tinos",serif;font-weight:700;font-size:27px;line-height:32px;color:var(--white)}
</style>
</head>
<body>
<main class="flyer">
  <div class="hero-photo" role="img" aria-label="Family gathered around an outdoor stone kitchen with a grill in a landscaped backyard"></div>
  <svg class="hero-mask" viewBox="0 0 794 560" aria-hidden="true">
    <path d="M0,0 H794 V82 Q397,239 0,100 Z" fill="#fff"/>
    <path d="M0,92 Q397,231 794,74" fill="none" stroke="#8cbf1f" stroke-width="2"/>
    <path d="M0,100 Q397,239 794,82" fill="none" stroke="#8cbf1f" stroke-width="5"/>
    <path d="M0,560 V522 Q397,384 794,517 V560 Z" fill="#fff"/>
    <path d="M0,522 Q397,384 794,517" fill="none" stroke="#8cbf1f" stroke-width="5"/>
    <path d="M0,533 Q397,397 794,528" fill="none" stroke="#8cbf1f" stroke-width="2"/>
  </svg>

  <div class="top-strip"></div>
  <svg class="title-banner" viewBox="0 0 794 64" aria-hidden="true">
    <polygon points="90,20 107,0 122,20" fill="#555"/>
    <polygon points="672,20 687,0 704,20" fill="#555"/>
    <polygon points="107,0 687,0 650,62 144,62" fill="#8cbf1f"/>
  </svg>
  <div class="brand-name">BRIGHTWELL CREW</div>

  <div class="tagline">
    <h2>PROVIDES A VARIETY HOME SERVICES</h2>
    <p>Focused on Cleaning &amp; Improving<br>The Exterior of The Home</p>
  </div>

  <div class="service-label left green" style="left:127px;top:540px;width:255px">POWER WASHING</div>
  <div class="service-photo" role="img" aria-label="Worker power washing a concrete driveway" style="left:24px;top:532px;background:linear-gradient(160deg,#9bb07a,#d9d6cc)"></div>
  <p class="service-text" style="left:169px;top:579px">Driveways, sidewalks,<br>patios, decks, fence</p>

  <div class="service-label left teal" style="left:127px;top:688px;width:255px">FENCE STAINING</div>
  <div class="service-photo green" role="img" aria-label="Brush applying stain to a wooden fence board" style="left:24px;top:680px;background:linear-gradient(100deg,#b8864f,#d9a66a 60%,#8ab0d8)"></div>
  <p class="service-text" style="left:173px;top:729px">Make fence look new with<br>variety of staining colors</p>

  <div class="service-label left green" style="left:127px;top:841px;width:255px">GUTTER CLEANING</div>
  <div class="service-photo" role="img" aria-label="Gutter filled with leaves and debris" style="left:24px;top:829px;background:linear-gradient(170deg,#e6e2dc,#a08a6a 60%,#7b7468)"></div>
  <p class="service-text" style="left:173px;top:880px">Important to make sure have<br>proper Water Drainage</p>

  <div class="service-label right teal small" style="left:404px;top:540px;width:280px">GUTTER GUARD INSTALLATION</div>
  <div class="service-photo green" role="img" aria-label="Mesh gutter guard installed along a roof edge" style="left:649px;top:532px;background:linear-gradient(135deg,#6e6a66,#a7a198 50%,#e8e8e8)"></div>
  <p class="service-text right" style="right:163px;top:579px">Prevent damage to roof and<br>house by keeping debris out of<br>gutters and water flowing.</p>

  <div class="service-label right green" style="left:414px;top:688px;width:270px;padding-left:54px">WINDOW WASHING</div>
  <div class="service-photo" role="img" aria-label="Worker cleaning an exterior window" style="left:649px;top:680px;background:linear-gradient(120deg,#8a9fb3,#d5dde3 55%,#c9b59a)"></div>
  <p class="service-text right" style="right:163px;top:729px">Our exterior washing team<br>and reach the highest windows</p>

  <div class="service-label right teal small" style="left:414px;top:841px;width:270px;padding-left:28px">LANDSCAPE &amp; PATIO LIGHTS</div>
  <div class="service-photo green" role="img" aria-label="Patio at dusk lit by string lights" style="left:649px;top:829px;background:linear-gradient(180deg,#2c3a4a,#4d5a48 55%,#8a7a5a)"></div>
  <p class="service-text right" style="right:163px;top:882px">Highlight areas<br>for beauty and safety</p>

  <footer class="footer">
    <div class="phone-pill">972-648-0000</div>
    <div class="call-label">CALL US</div>
    <div class="website">www.brightwellcrew.com</div>
  </footer>
</main>
</body>
</html>
```